Business logo & card design needed

We need a business logo & card design for a new company in NSW called 'Tallow Ridge Solutions'.
The company provides electrical services such as; electrical/refrigeration & air conditioning/data/security/audio visual entertainment/design & install.
We would like a logo which can relate to the electrical industry.
Updates

Industry/Entity Type

Electrical

Contact Information for Business Card

Tallow Ridge Solutions
Lira Mostfeld, Ph: 0471958360, Lic: 562930K

Logo Text

Tallow Ridge Solutions

Logo styles of interest
Emblem Logo
Abstract Logo
Wordmark Logo
Requirements
Must have
• The card must include the services we provide; electrical/refrigeration & air conditioning/data/security/audio visual entertainment/design & install.
It must also include the licence number; Lic: 562930K

```html
<!DOCTYPE html>
<html lang="en">
<head>
<meta charset="utf-8">
<title>Tallow Ridge Solutions – Business Card</title>
<link rel="stylesheet" href="https://fonts.googleapis.com/css2?family=Arimo:wght@400;700&display=swap">
<style>
  :root {
    --backdrop: #d9d9d7;
    --card: #1f1e1f;
    --card-edge: #2a292a;
    --brand-blue: #1f7fd0;
    --brand-green: #8cc63f;
    --text-light: #f2f2f2;
  }
  * { box-sizing: border-box; margin: 0; padding: 0; }
  html, body {
    width: 1200px;
    height: 900px;
    overflow: hidden;
    background: var(--backdrop);
    font-family: "Arimo", Arial, sans-serif;
  }
  .canvas {
    position: relative;
    width: 1200px;
    height: 900px;
  }
  .card {
    position: absolute;
    width: 620px;
    height: 378px;
    background: var(--card);
    border: 1px solid var(--card-edge);
    border-radius: 22px;
    box-shadow: 0 10px 28px rgba(0,0,0,.28);
    overflow: hidden;
  }
  .card--back { left: 150px; top: 50px; }
  .card--front { left: 430px; top: 470px; }

  .wordmark {
    display: flex;
    align-items: center;
    gap: 12px;
    color: var(--brand-blue);
    font-weight: 700;
    font-size: 38px;
    letter-spacing: .5px;
    white-space: nowrap;
  }
  .wordmark__dot {
    width: 18px;
    height: 18px;
    border-radius: 50%;
    background: var(--brand-green);
    flex: none;
  }
  .card--back .wordmark {
    position: absolute;
    left: 0; right: 0; top: 86px;
    justify-content: center;
  }
  .card--front .wordmark {
    position: absolute;
    left: 40px; top: 52px;
    font-size: 34px;
  }

  .services {
    position: absolute;
    left: 0; right: 0; top: 200px;
    text-align: center;
    color: var(--brand-blue);
    font-size: 17px;
    letter-spacing: 1.6px;
    line-height: 1.45;
  }
  .sep {
    display: inline-block;
    width: 2px;
    height: 17px;
    margin: 0 8px;
    background: var(--brand-green);
    vertical-align: -2px;
  }

  .contact {
    position: absolute;
    left: 336px; top: 176px;
    color: var(--text-light);
  }
  .contact__name {
    color: var(--brand-green);
    font-size: 24px;
    letter-spacing: 1px;
    margin-bottom: 10px;
  }
  .contact__row {
    display: flex;
    font-size: 13px;
    letter-spacing: 1px;
    line-height: 1.55;
  }
  .contact__label {
    width: 34px;
    color: #cfcfcf;
  }
  .accent-bar {
    position: absolute;
    width: 12px;
  }
  .accent-bar--green { right: 0; top: 170px; height: 82px; background: var(--brand-green); }
  .accent-bar--blue { left: 0; top: 296px; height: 34px; background: var(--brand-blue); }

  .markets {
    position: absolute;
    left: 40px; bottom: 34px;
    color: var(--brand-blue);
    font-size: 16px;
    letter-spacing: 1.6px;
  }
</style>
</head>
<body>
<main class="canvas">

  <section class="card card--back" aria-label="Business card, back">
    <div class="wordmark">Tallow Ridge Solutions<span class="wordmark__dot"></span></div>
    <p class="services">
      Electrical<span class="sep"></span>Refrigeration<span class="sep"></span>Air conditioning<br>
      Data<span class="sep"></span>Security<span class="sep"></span>Audio visual entertainment<br>
      Design &amp; Install
    </p>
  </section>

  <section class="card card--front" aria-label="Business card, front">
    <div class="wordmark">Tallow Ridge Solutions<span class="wordmark__dot"></span></div>
    <div class="contact">
      <p class="contact__name">Lira Mostfeld</p>
      <p class="contact__row"><span class="contact__label">P:</span>0471 958 360</p>
      <p class="contact__row"><span class="contact__label">E:</span>tallowridge.solutions@mailbox.com</p>
      <p class="contact__row"><span class="contact__label">Lic:</span>562930K</p>
    </div>
    <span class="accent-bar accent-bar--green"></span>
    <span class="accent-bar accent-bar--blue"></span>
    <p class="markets">Residential<span class="sep"></span>Commercial<span class="sep"></span>Industrial</p>
  </section>

</main>
</body>
</html>
```